FinTech company looking to revamp and expand client-facing interface for our financial models

Halvern Quotient currently has a very simple website that allows clients to interact with our financial models. We are looking to completely redesign the current site and add several extra pages to provide extra functionality. We want the design to have a modern, slick feel, that will work on both a desktop or a tablet. It should be straightforward for clients to move between different pages at any time, and clear from the layout how to interact with the more advanced features. We have included screenshots of existing pages in the attached design brief, as well as sketches of the functionality required by the new pages, but can't provide a direct link to the current site.
Target Market(s)
Professional investors that will be paying to access the interface
Industry/Entity Type
Finance
Number of Pages Required
4 page
Colors
Designer to choose colors to be used in the design.
Look and feel
Each slider illustrates characteristics of the customer's brand and the style your logo design should communicate.

```html
<!DOCTYPE html>
<html lang="en">
<head>
<meta charset="utf-8">
<title>QMETRIC – Sensitivities</title>
<link href="https://fonts.googleapis.com/css2?family=Open+Sans:wght@400;600;700&display=swap" rel="stylesheet">
<style>
  :root {
    --teal: #00695f;
    --teal-soft: #e2f2ee;
    --ink: #1a1a1a;
    --text: #222222;
    --white: #ffffff;
    --tab-gray: #d6d6d6;
    --bg-top: #e6e6e6;
    --bg-bottom: #f8f8f8;
    --line: #e4e4e4;
    --navy: #12355b;
  }
  * { box-sizing: border-box; margin: 0; padding: 0; }
  html, body { width: 1200px; height: 678px; overflow: hidden; }
  body {
    font-family: "Open Sans", Arial, sans-serif;
    color: var(--text);
    background: linear-gradient(180deg, var(--bg-top) 0%, var(--bg-bottom) 100%);
    position: relative;
  }

  /* Top bar */
  .topbar {
    position: absolute; left: 0; top: 0; width: 1200px; height: 55px;
    background: var(--white); box-shadow: 0 3px 8px rgba(0,0,0,.08);
    display: flex; align-items: stretch;
  }
  .brand {
    position: absolute; left: 67px; top: 0; height: 55px;
    display: flex; align-items: center;
    font-weight: 700; font-size: 17px; color: var(--ink); letter-spacing: .3px;
  }
  .period-switch { position: absolute; left: 180px; top: 0; display: flex; height: 55px; }
  .period {
    width: 83px; display: flex; align-items: center; justify-content: center;
    font-weight: 600; font-size: 13px; color: var(--ink); border-right: 1px solid #eee;
  }
  .period.is-active { background: var(--teal); color: var(--white); }
  .main-nav { position: absolute; left: 555px; top: 0; display: flex; height: 55px; }
  .nav-item {
    display: flex; align-items: center; justify-content: center; gap: 7px;
    font-weight: 700; font-size: 12.5px; color: var(--ink);
    border-left: 1px solid #eee;
  }
  .nav-item:last-child { border-right: 1px solid #eee; }
  .nav-item.is-active { background: var(--teal); color: var(--white); }
  .nav-item svg { width: 24px; height: 24px; }

  /* Sub tabs */
  .subtabs { position: absolute; left: 0; top: 0; }
  .subtab {
    position: absolute; bottom: auto; background: var(--white);
    border-radius: 5px 5px 0 0;
    display: flex; align-items: center; justify-content: center;
    font-weight: 700; font-size: 12px; color: var(--ink);
  }
  .subtab.is-muted { background: var(--tab-gray); }
  .subtab-icon { background: var(--white); border-radius: 5px 5px 0 0; position: absolute; display: flex; align-items: center; justify-content: center; }

  /* Export */
  .export {
    position: absolute; left: 1084px; top: 183px;
    display: flex; align-items: center; gap: 6px;
    font-weight: 700; font-size: 15px; color: var(--teal);
  }

  /* Table */
  .data-table {
    position: absolute; left: 97px; top: 217px; width: 1071px;
    border-collapse: collapse; background: var(--white);
    border-radius: 7px; overflow: hidden;
    box-shadow: 0 2px 10px rgba(0,0,0,.1);
    table-layout: fixed;
  }
  .data-table th, .data-table td { text-align: center; border-right: 1px solid var(--line); }
  .data-table th:last-child, .data-table td:last-child { border-right: none; }
  .data-table th {
    height: 65px; font-weight: 700; font-size: 15.5px; color: var(--white);
  }
  .data-table th.col-key { background: var(--ink); border-right-color: #3a3a3a; }
  .data-table th.col-stat { background: var(--teal); border-right-color: #1b7b71; }
  .data-table td { height: 63px; font-size: 15.5px; color: var(--ink); }
  .data-table tbody tr:nth-child(even) td { background: var(--teal-soft); }
  .data-table td.num { text-align: left; padding-left: 28px; }
  .sort-caret { display: inline-block; vertical-align: middle; margin-left: 4px; }

  /* Filters drawer */
  .filters {
    position: absolute; left: 0; top: 295px; width: 46px; height: 231px;
    background: #d3d3d3; border-radius: 0 4px 4px 0;
  }
  .filters-label {
    position: absolute; left: 8px; top: 150px; transform: rotate(-90deg); transform-origin: left top;
    font-weight: 700; font-size: 14.5px; letter-spacing: 1px; color: var(--ink);
  }
  .filters-toggle { position: absolute; left: 33px; top: 398px; }
</style>
</head>
<body>

<header class="topbar">
  <div class="brand">QMETRIC</div>
  <nav class="period-switch">
    <div class="period is-active">250D</div>
    <div class="period">83D</div>
    <div class="period">42D</div>
  </nav>
  <nav class="main-nav">
    <div class="nav-item" style="width:129px">
      <svg viewBox="0 0 24 24"><path d="M3 11.5 12 4l9 7.5" fill="none" stroke="#1a1a1a" stroke-width="2.4" stroke-linejoin="round"/><path d="M5.5 10v10h5v-5h3v5h5V10" fill="#1a1a1a"/></svg>
      MODELS
    </div>
    <div class="nav-item is-active" style="width:164px">
      <svg viewBox="0 0 24 24" fill="none" stroke="#fff" stroke-width="1.4"><circle cx="12" cy="12" r="3"/><circle cx="12" cy="12" r="7" stroke-dasharray="2 2"/><path d="M12 2v3M12 19v3M2 12h3M19 12h3M5 5l2 2M17 17l2 2M5 19l2-2M17 7l2-2"/></svg>
      SENSITIVITIES
    </div>
    <div class="nav-item" style="width:148px">
      <svg viewBox="0 0 24 24" fill="none" stroke="#1a1a1a" stroke-width="1.8"><circle cx="7" cy="7" r="4"/><circle cx="17" cy="7" r="4"/><circle cx="7" cy="17" r="4"/><circle cx="17" cy="17" r="4"/></svg>
      PORTFOLIO
    </div>
    <div class="nav-item" style="width:139px">
      <svg viewBox="0 0 24 24" fill="none" stroke="#1a1a1a" stroke-width="1.8"><rect x="3" y="4" width="18" height="16"/><path d="M5 16l4-5 3 3 3-5 4 4" stroke-linejoin="round"/></svg>
      BACKTEST
    </div>
  </nav>
</header>

<nav class="subtabs">
  <div class="subtab is-muted" style="left:65px;top:111px;width:143px;height:32px">EQUITIES</div>
  <div class="subtab" style="left:212px;top:111px;width:143px;height:32px">ETFS</div>
  <div class="subtab" style="left:360px;top:102px;width:143px;height:41px">PAIRS</div>
  <div class="subtab is-muted" style="left:508px;top:92px;width:143px;height:51px">ETF PAIRS
    <svg style="position:absolute;left:111px;top:23px" width="22" height="26" viewBox="0 0 22 26"><path d="M6 2.5a1.6 1.6 0 0 1 3.2 0V12l1-.1V9.6a1.6 1.6 0 0 1 3.1 0v2.6l.9.1v-1.8a1.6 1.6 0 0 1 3.1 0v2.3l.6.1a1.6 1.6 0 0 1 3.1 0V18c0 4-2.7 6.5-6.5 6.5H11c-2.4 0-3.8-1-5-2.7L1.6 15.4a1.6 1.6 0 0 1 2.6-1.8L6 15.6z" fill="#fff" stroke="#1a1a1a" stroke-width="1.3" stroke-linejoin="round"/></svg>
  </div>
  <div class="subtab" style="left:656px;top:102px;width:143px;height:41px">FACTORS</div>
  <div class="subtab" style="left:803px;top:111px;width:143px;height:32px">NEW TAB TITLE #1</div>
  <div class="subtab" style="left:951px;top:111px;width:143px;height:32px">NEW TAB TITLE #2</div>
  <div class="subtab-icon" style="left:1099px;top:111px;width:37px;height:32px">
    <svg width="12" height="16" viewBox="0 0 12 16"><path d="M3 2l6 6-6 6" fill="none" stroke="#6b6b6b" stroke-width="2.6"/></svg>
  </div>
  <div class="subtab-icon" style="left:1140px;top:111px;width:37px;height:32px">
    <svg width="22" height="22" viewBox="0 0 22 22"><circle cx="11" cy="11" r="9.5" fill="none" stroke="#6b6b6b" stroke-width="1.6"/><path d="M11 6v10M6 11h10" stroke="#6b6b6b" stroke-width="1.6"/></svg>
  </div>
</nav>

<div class="export">
  <svg width="24" height="22" viewBox="0 0 24 22" fill="none" stroke="#00695f" stroke-width="2"><path d="M10 4H3v16h16v-6"/><path d="M8 15c1-5 5-8 11-8"/><path d="M15 3l5 4-4 4" stroke-linejoin="round"/></svg>
  Export
</div>

<table class="data-table">
  <colgroup>
    <col style="width:138px"><col style="width:92px"><col style="width:177px">
    <col style="width:83px"><col style="width:83px"><col style="width:83px"><col style="width:83px">
    <col style="width:83px"><col style="width:83px"><col style="width:83px"><col style="width:83px">
  </colgroup>
  <thead>
    <tr>
      <th class="col-key">Factor</th>
      <th class="col-key">ID<svg class="sort-caret" width="10" height="7" viewBox="0 0 10 7"><path d="M1 1l4 4 4-4" fill="none" stroke="#fff" stroke-width="1.8"/></svg></th>
      <th class="col-key">Sector</th>
      <th class="col-stat">Stat 1</th><th class="col-stat">Stat 2</th><th class="col-stat">Stat 3</th><th class="col-stat">Stat 4</th>
      <th class="col-stat">Stat 5</th><th class="col-stat">Stat 6</th><th class="col-stat">Stat 7</th><th class="col-stat">Stat 8</th>
    </tr>
  </thead>
  <tbody>
    <tr><td>Factor 1</td><td>Model 1</td><td>Materials</td><td class="num">-1.4</td><td class="num">0.1</td><td class="num">-3.1</td><td class="num">0.7</td><td class="num">30.2</td><td class="num">0.9</td><td class="num">-3.1</td><td class="num">0.1</td></tr>
    <tr><td>Factor 2</td><td>Model 2</td><td>Materials</td><td class="num">2.8</td><td class="num">0.1</td><td class="num">6.1</td><td class="num">100</td><td class="num">30.2</td><td class="num">0.9</td><td class="num">6.1</td><td class="num">0.1</td></tr>
    <tr><td>Factor 3</td><td>Model 3</td><td>Materials</td><td class="num">-3.7</td><td class="num">2.7</td><td class="num">-7.2</td><td class="num">100</td><td class="num">30.2</td><td class="num">0.9</td><td class="num">-7.2</td><td class="num">2.7</td></tr>
    <tr><td>Factor 4</td><td>Model 4</td><td>Industrials</td><td class="num">2.8</td><td class="num">0.2</td><td class="num">2.7</td><td class="num">0.5</td><td class="num">32.9</td><td class="num">-0.5</td><td class="num">2.7</td><td class="num">0.2</td></tr>
    <tr><td>Factor 5</td><td>Model 5</td><td>Industrials</td><td class="num">0.8</td><td class="num">0.3</td><td class="num">2.5</td><td class="num">0.5</td><td class="num">32.9</td><td class="num">-0.5</td><td class="num">2.5</td><td class="num">0.3</td></tr>
  </tbody>
</table>

<aside class="filters">
  <span class="filters-label">FILTERS</span>
</aside>
<svg class="filters-toggle" width="27" height="27" viewBox="0 0 27 27">
  <circle cx="13.5" cy="13.5" r="12.5" fill="#12355b" stroke="#fff" stroke-width="1.5"/>
  <path d="M7.5 13.5h11M14 9l4.5 4.5L14 18" fill="none" stroke="#fff" stroke-width="2" stroke-linecap="round" stroke-linejoin="round"/>
</svg>

</body>
</html>
```